Business card, postcard, pocket folder

We are a real estate team and have had a new logo designed. From this, we need the following deliverables:- Business Cards (double-sided)- Just Listed / Just Sold Postcards (double-sided)- Pocket Folder. See logo attached.More work possible for the winning designer.
There are 5 members of the team, so head shots should be easily changed and possible for a group photo might be a good idea for the pocket folder but not 100% neccessary.
Target Market(s)
Real estate
Industry/Entity Type
Real Estate
Font styles to use
Serif
Sans Serif
Requirements
Must have
- Business cards and postcards must have a head shot on them.

```html
<!DOCTYPE html>
<html lang="en">
<head>
<meta charset="UTF-8">
<title>Hartwell Group Pocket Folder</title>
<link href="https://fonts.googleapis.com/css2?family=Mulish:ital,wght@0,400;0,600;1,400&display=swap" rel="stylesheet">
<style>
  :root {
    --page-bg: #2b2b2b;
    --paper: #ffffff;
    --brand-blue: #243a8f;
    --brand-red: #d71f2a;
    --ink-light: #ffffff;
    --photo-dark: #1d1f24;
    --photo-mid: #4a5566;
  }
  * { box-sizing: border-box; margin: 0; padding: 0; }
  html, body {
    width: 1189px; height: 1200px; overflow: hidden;
    background: var(--page-bg);
    font-family: "Mulish", sans-serif;
  }
  .folder {
    position: absolute; left: 64px; top: 150px;
    width: 1060px; height: 900px;
    background: var(--paper);
    overflow: hidden;
  }
  .cover-top { position: absolute; left: 0; top: 0; width: 100%; height: 355px; }
  .brand {
    position: absolute; left: 700px; top: 190px;
    display: flex; align-items: center; gap: 10px;
    color: var(--brand-blue); font-size: 38px; font-weight: 600;
    letter-spacing: -0.5px;
  }
  .brand-mark { width: 22px; height: 22px; background: var(--brand-blue); }
  .stripe-red-top { position: absolute; left: 0; top: 355px; width: 100%; height: 11px; background: var(--brand-red); }
  .team-photo {
    position: absolute; left: 0; top: 372px; width: 100%; height: 348px;
    background: linear-gradient(180deg, var(--photo-mid) 0%, var(--photo-dark) 55%, #2a3550 100%);
  }
  .contact-band {
    position: absolute; left: 0; top: 726px; width: 100%; height: 110px;
    background: var(--brand-blue); color: var(--ink-light);
  }
  .contact-list {
    position: absolute; left: 40px; top: 44px;
    display: flex; align-items: center;
  }
  .contact-item {
    display: flex; align-items: center; gap: 7px;
    font-size: 10.5px; line-height: 1.3;
    padding: 0 14px;
  }
  .contact-item + .contact-item { border-left: 2px solid var(--ink-light); }
  .contact-item:first-child { padding-left: 0; }
  .contact-item svg { width: 18px; height: 18px; flex: none; }
  .tagline {
    position: absolute; left: 640px; top: 28px; width: 320px;
    text-align: center; font-style: italic; font-size: 17px; line-height: 1.3;
  }
  .stripe-red-bottom {
    position: absolute; left: 0; top: 840px; width: 100%; height: 60px;
    background: var(--brand-red);
  }
  .social-list { position: absolute; left: 215px; top: 18px; display: flex; gap: 9px; }
  .social-list span { width: 15px; height: 15px; background: var(--ink-light); display: block; }
  .web-address {
    position: absolute; left: 700px; top: 20px; width: 240px; text-align: center;
    color: var(--ink-light); font-size: 10.5px; letter-spacing: 4px;
  }
</style>
</head>
<body>
  <div class="folder">
    <section class="cover-top">
      <div class="brand"><span class="brand-mark"></span>Hartwell Group</div>
    </section>

    <div class="stripe-red-top"></div>

    <div class="team-photo" role="img" aria-label="Group photo of the real estate team in an office"></div>

    <section class="contact-band">
      <div class="contact-list">
        <div class="contact-item">
          <svg viewBox="0 0 20 20"><circle cx="10" cy="10" r="9" fill="none" stroke="#fff" stroke-width="1.6"/><path d="M7 5.5c-1 .5-1.3 1.8-.6 3.2 1 2 2.6 3.7 4.6 4.7 1.3.6 2.6.4 3.1-.6l-1.6-1.6-1.3.7c-1-.5-2-1.5-2.5-2.5l.7-1.3z" fill="#fff"/></svg>
          <div>Mobile: (555) 201-4480<br>Office: (555) 201-4481</div>
        </div>
        <div class="contact-item">
          <svg viewBox="0 0 20 20"><circle cx="10" cy="10" r="9" fill="none" stroke="#fff" stroke-width="1.6"/><circle cx="10" cy="10" r="5.5" fill="none" stroke="#fff" stroke-width="1.2"/><ellipse cx="10" cy="10" rx="2.3" ry="5.5" fill="none" stroke="#fff" stroke-width="1"/><path d="M4.5 10h11" stroke="#fff" stroke-width="1"/></svg>
          <div>info@hartwellgroup.com<br>www.hartwellgroup.com</div>
        </div>
        <div class="contact-item">
          <svg viewBox="0 0 20 20"><circle cx="10" cy="10" r="9" fill="none" stroke="#fff" stroke-width="1.6"/><path d="M10 4.5a3.5 3.5 0 0 0-3.5 3.5c0 2.6 3.5 7 3.5 7s3.5-4.4 3.5-7A3.5 3.5 0 0 0 10 4.5z" fill="#fff"/><circle cx="10" cy="8" r="1.3" fill="#243a8f"/></svg>
          <div>PO BOX 48, 14 Linden Street<br>Ballarat, Australia</div>
        </div>
      </div>
      <p class="tagline">Lorem Ipsum is simply dummy text of the printing and typesetting industry..</p>
    </section>

    <section class="stripe-red-bottom">
      <div class="social-list"><span></span><span></span><span></span></div>
      <p class="web-address">www.HARTWELLGROUP.com</p>
    </section>
  </div>
</body>
</html>
```